Establishing a website for a non profit organisation

The foundation is called:

German: Edle Alte Bruderschaft des Hofes Lindenmark e.V.

Englisch (Translation): Noble old Brotherhood of Court Lindenmark e.V.

The foundation is a legal nonprofit organization with the purpose to help people in need. The foundation - a charitable organization - donates funds and supports solely and directly people living in Frankfurt and in Germany.

In some cases the foundation works together with other charitable organizations that support projects to help people in need.

The foundation also functions as trustee with powers of administration of property in trust with a legal obligation to administer it solely for the purposes specified. The purpose is not to generate/obtain wealth for shareholders but to respectfully execute the benevolent intentions of the founders/testators in the interest of the legatee.

The foundation was established in 1408.

The website should give a good and easy overview about the foundation work.
It should be easy to figure out how to participate and help the organisation.
Either you can participate with a one time donation, with a regular donation or with a testament.

For those with donation it is possible to hand over an contribution receipt for tax purposes.

The main color should be red: RGB R:229 - G:47 - B:34

```html
<!DOCTYPE html>
<html lang="en">
<head>
<meta charset="utf-8">
<title>Noble old Brotherhood of Court Lindenmark e.V.</title>
<link href="https://fonts.googleapis.com/css2?family=Overlock:wght@400;700&family=Advent+Pro:wght@500&family=Michroma&display=swap" rel="stylesheet">
<style>
:root{
  --red:#e52f22;
  --red-dark:#c9271c;
  --header:#232323;
  --cream:#f8f3ed;
  --text:#555;
  --muted:#bdbdbd;
  --white:#fff;
}
*{margin:0;padding:0;box-sizing:border-box}
html,body{width:1200px;height:999px;overflow:hidden}
body{position:relative;background:var(--cream);font-family:"Overlock",sans-serif;color:var(--text)}
h1,h2{font-weight:400}
.abs{position:absolute}
.site-header{left:0;top:0;width:1200px;height:102px;background:var(--header)}
.brand-mark{left:105px;top:11px;width:78px;height:78px;border:3px solid var(--red);border-radius:50%}
.brand-name{left:205px;top:25px;color:var(--white);font-size:26px;line-height:30px}
.contact{right:103px;text-align:right;font-size:15px;color:var(--muted);white-space:nowrap}
.contact span{color:var(--white)}
.contact.phone{top:10px}
.contact.mail{top:37px}
.social{right:103px;top:71px;display:flex;gap:7px}
.social i{display:block;width:17px;height:17px;background:#8a8a8a;border-radius:2px}
.social i:first-child{background:var(--red)}
.main-nav{left:0;top:102px;width:1200px;height:50px;background:var(--red);border-bottom:1px solid #7a1a12}
.tagline{left:163px;top:118px;color:var(--white);font-size:15px;white-space:nowrap}
.nav-active{left:515px;top:102px;width:48px;height:57px;background:var(--red-dark)}
.nav-item{top:118px;font-size:15px;color:var(--white);white-space:nowrap}
.hero{left:0;top:152px;width:1200px;height:555px;background:radial-gradient(ellipse at 72% 45%,#8a6a55 0%,#5e4d42 35%,#6d6660 70%,#4a4541 100%)}
.hero-title{left:60px;top:318px;width:554px;text-align:center;font-family:"Advent Pro",sans-serif;font-weight:500;font-size:28px;line-height:47px;letter-spacing:0.5px;color:#f3ece4;white-space:nowrap}
.hero-text{left:120px;top:425px;width:434px;text-align:center;font-size:15px;line-height:30px;color:var(--white)}
.arrow{width:42px;height:48px;top:358px}
.dots{left:114px;top:640px;display:flex;gap:10px}
.dots i{display:block;width:10px;height:10px;border-radius:50%;background:#eee}
.dots i.on{background:var(--red)}
.feature-image{left:100px;top:727px;width:632px;height:169px;background:linear-gradient(100deg,#3b3b3b 0%,#7d7d7d 45%,#c9c9c9 80%,#a9a9a9 100%)}
.feature-caption{left:117px;top:803px;font-family:"Michroma",sans-serif;font-size:21.5px;line-height:31px;color:var(--white);white-space:nowrap}
.copy{font-size:14px;line-height:21px;text-align:justify;color:#5a5a5a}
.copy em{font-style:normal;color:var(--red)}
.copy.left{left:101px;top:900px;width:626px}
.copy.right{left:756px;top:801px;width:341px}
.section-title{left:756px;top:724px;font-size:22px;line-height:30px;color:#444;text-transform:uppercase;white-space:nowrap}
.btn{top:948px;width:98px;height:37px;background:var(--red);color:var(--white);font-size:13px;line-height:37px;text-align:center}
.rule{top:994px;height:0;border-top:2px dotted #cfc9c2}
</style>
</head>
<body>
<header class="abs site-header">
  <div class="abs brand-mark"></div>
  <div class="abs brand-name">Noble old Brotherhood of<br>Court Lindenmark e.V.</div>
  <div class="abs contact phone">Telephone : <span>+49 30 5550 1408</span></div>
  <div class="abs contact mail">E-mail : <span>kontakt@lindenmark-stiftung.example</span></div>
  <div class="abs social"><i></i><i></i><i></i><i></i><i></i><i></i></div>
</header>

<nav class="abs main-nav"></nav>
<div class="abs tagline">The foundation was established in 1408.</div>
<div class="abs nav-active"></div>
<div class="abs nav-item" style="left:519px">HOME</div>
<div class="abs nav-item" style="left:593px">ABOUT US</div>
<div class="abs nav-item" style="left:692px">FEATURES</div>
<div class="abs nav-item" style="left:788px">MEDIA</div>
<div class="abs nav-item" style="left:863px">BLOG</div>
<div class="abs nav-item" style="left:931px">EVENTS</div>
<div class="abs nav-item" style="left:1012px">SHORTCODES</div>

<section class="abs hero" role="img" aria-label="Photograph of a child with folded hands looking upward in prayer"></section>
<h1 class="abs hero-title">BECOMING WHO GOD CREATED US TO BE<br>SEEK SERVE SHARE</h1>
<p class="abs hero-text">Lorem ipsum dolor sit amet, consectetuer adipiscing elit. Aenean commodo ligula eget dolor. Aenean massa.</p>
<svg class="abs arrow" style="left:34px" viewBox="0 0 42 48"><circle cx="21" cy="24" r="20" fill="var(--red)" stroke="#fff" stroke-width="2.5"/><path d="M24 16 L16 24 L24 32" fill="none" stroke="#fff" stroke-width="3.5" stroke-linecap="round" stroke-linejoin="round"/></svg>
<svg class="abs arrow" style="left:1123px" viewBox="0 0 42 48"><circle cx="21" cy="24" r="20" fill="var(--red)" stroke="#fff" stroke-width="2.5"/><path d="M18 16 L26 24 L18 32" fill="none" stroke="#fff" stroke-width="3.5" stroke-linecap="round" stroke-linejoin="round"/></svg>
<div class="abs dots"><i></i><i></i><i class="on"></i><i></i></div>

<div class="abs feature-image" role="img" aria-label="Black and white photograph of two hands clasped together"></div>
<h2 class="abs feature-caption">Together we create<br>a special world</h2>
<p class="abs copy left"><em>Lorem ipsum dolor sit amet, consectetuer</em> adipiscing elit. Aenean commodo ligula eget dolor. Aenean massa. Cum sociis natoque penatibus et magnis dis parturient montes, nascetur ridiculus mus.</p>
<div class="abs btn" style="left:101px">READ MORE</div>
<div class="abs rule" style="left:101px;width:626px"></div>

<h2 class="abs section-title">Rasing funds for<br>rehabilitation services</h2>
<p class="abs copy right">Lorem ipsum dolor sit amet, consectetuer adipiscing elit. Aenean commodo ligula eget dolor. Aenean massa. Cum sociis natoque penatibus et magnis dis parturient montes, nascetur ridiculus mus. Donec quam felis, ultricies nec, pellentesque eu, pretium quis, sem. justo. Nullam dictum felis eu pede mollis</p>
<div class="abs btn" style="left:757px">READ MORE</div>
<div class="abs rule" style="left:757px;width:340px"></div>
</body>
</html>
```